Day Spa Web Design Project

We just created a blog to add to our main site. We need the colors to match our main site and the look and feel of the blog to be smoother and less ameture looking, like the examples below.

Main Site, match this color scheme:
http://www.fernlowdayspa.com/

The project site:
http://blog.fernlowdayspa.com/

Our industry leaders blog site is our comparative and examples of what we need:
http://blog.relaxquest.com/
http://blog.purewellnessjournal.com/
http://thecoralbayblog.com/ (i like the layout a lot)
http://www.kneadhaven.com/blog/

Requirements
Must have
• social sharing.
Responsive design (already has it just keep it)
appealing mobile front page

```html
<!DOCTYPE html>
<html lang="en">
<head>
<meta charset="utf-8">
<title>Fernlow Day Spa – Blog</title>
<link href="https://fonts.googleapis.com/css2?family=PT+Sans:wght@400;700&family=PT+Serif&family=Open+Sans:wght@300;400&display=swap" rel="stylesheet">
<style>
:root{
  --page-bg:#ecca93;
  --page-band:#d9ae6c;
  --sheet:#f7e5c8;
  --sheet-light:#f9ecd6;
  --panel:#fbf0de;
  --panel-line:#e9d3b0;
  --ink:#2a1d10;
  --body:#4a3a2a;
  --header:#000;
  --nav-top:#3d2c18;
  --nav-bottom:#1b1209;
  --nav-sep:#5a4328;
  --white:#fff;
  --button:#2b1d0e;
  --rule:#e2cca6;
}
*{box-sizing:border-box;margin:0;padding:0}
html,body{width:848px;height:1200px;overflow:hidden}
body{
  position:relative;
  background:linear-gradient(180deg,var(--page-bg) 0,#e6bd7f 98px,var(--page-band) 118px,#f0d3a2 170px,var(--page-bg) 400px,#f2d6a9 1200px);
  font-family:"Open Sans",sans-serif;color:var(--body);
}
.sheet{
  position:absolute;left:50px;top:10px;width:748px;height:1104px;
  background:linear-gradient(180deg,var(--sheet) 0,var(--sheet-light) 100%);
}
.masthead{
  position:absolute;left:0;top:0;width:748px;height:88px;
  background:var(--header);border-radius:5px 5px 0 0;
}
.brand{position:absolute;left:36px;top:24px;color:var(--white);font-family:"PT Sans",sans-serif;font-weight:400}
.brand-name{font-size:28px;line-height:1}
.brand-tag{font-size:12px;margin-top:4px}
.callout{position:absolute;right:23px;top:34px;text-align:right;color:var(--white);font-family:"PT Sans",sans-serif}
.callout-label{font-size:14px;line-height:1}
.callout-phone{font-size:22px;line-height:1.15}
.main-nav{
  position:absolute;left:0;top:88px;width:748px;height:40px;
  background:linear-gradient(180deg,var(--nav-top),var(--nav-bottom));
  display:flex;padding-left:6px;
}
.main-nav a{
  color:var(--white);text-decoration:none;font-family:"PT Sans",sans-serif;font-size:13.5px;
  line-height:40px;padding:0 13px;border-right:1px solid var(--nav-sep);
}
.main-nav a:last-child{border-right:0}
.hero{
  position:absolute;left:16px;top:138px;width:720px;height:226px;
  border:2px solid #f4e6cf;
  background:linear-gradient(90deg,#6b5a4a 0,#9a8a78 30%,#cfc7b8 50%,#3a3530 70%,#e8c21e 88%,#f5d840 100%);
}
.page-title{position:absolute;left:17px;top:384px;font-family:"PT Sans",sans-serif;font-size:19px;color:var(--ink);font-weight:400}
.posts{
  position:absolute;left:14px;top:414px;width:518px;height:674px;
  background:var(--panel);border:1px solid var(--panel-line);padding:20px 20px 0 20px;
}
.post{margin-bottom:30px}
.post::after{content:"";display:block;clear:both}
.post-media{
  float:left;width:201px;height:119px;margin:0 14px 6px 0;
  border:3px solid #fff;box-shadow:0 0 2px rgba(0,0,0,.15);
}
.media-massage{background:linear-gradient(90deg,#c9a8b4,#e8d8d2 40%,#f2ece6 70%,#d8c6bc)}
.media-fashion{background:linear-gradient(90deg,#e25a2a 0,#f0c030 30%,#f3e9d8 33%,#d8b070 50%,#e8c8a8 66%,#2a5a70 68%,#f0a8c8 85%,#d860a0 100%)}
.post-title{font-family:"PT Serif",serif;font-size:13px;font-weight:400;color:var(--ink);text-transform:uppercase;margin:4px 0 6px}
.post p{font-size:8.1px;line-height:16px;font-weight:300;color:var(--body)}
.post p.clear{clear:both;padding-top:2px}
.post p.gap{margin-top:16px}
.share{display:flex;gap:4px;align-items:center;margin:8px 0 12px;clear:both}
.share span{width:15px;height:15px;border-radius:2px}
.share .s1{background:#3b5a9a}.share .s2{background:#d0422d}.share .s3{background:#3aa0d8}
.share .s4{background:#d8d8d8}.share .s5{background:#9aa0a8}.share .s6{background:#2aa6d8}
.share .count{width:auto;height:15px;padding:0 6px;background:#fff;border:1px solid #ddd;font-size:8px;line-height:13px;color:#333}
.more{
  display:inline-block;background:var(--button);color:var(--white);font-family:"PT Sans",sans-serif;
  font-size:9px;padding:0 10px;line-height:18px;border-radius:2px;text-decoration:none;
}
.sidebar{position:absolute;left:552px;top:414px;width:164px}
.sidebar h3{font-family:"PT Sans",sans-serif;font-weight:400;font-size:16px;color:var(--ink);margin:9px 0 5px}
.sidebar ul{list-style:none;margin-bottom:22px}
.sidebar li{
  font-size:8.3px;line-height:21.5px;border-bottom:1px solid var(--rule);color:var(--ink);
  padding-left:12px;position:relative;white-space:nowrap;
}
.sidebar li:last-child{border-bottom:0}
.sidebar li::before{content:"";position:absolute;left:2px;top:8px;border:3px solid transparent;border-left:4px solid var(--ink);border-right:0}
.site-footer{position:absolute;left:0;top:1133px;width:848px;text-align:center}
.footer-nav{font-family:"PT Sans",sans-serif;font-size:10.5px;color:var(--ink)}
.footer-nav a{color:var(--ink);text-decoration:none;margin:0 5px}
.copyright{font-size:8.5px;margin-top:12px;color:var(--body)}
.footer-social{position:absolute;left:697px;top:1129px;display:flex;gap:3px}
.footer-social span{width:20px;height:20px;border-radius:50%;background:#000}
</style>
</head>
<body>
<div class="sheet">
  <header class="masthead">
    <div class="brand">
      <div class="brand-name">Fernlow Day Spa</div>
      <div class="brand-tag">Massage, Facials &amp; Quiet Afternoons</div>
    </div>
    <div class="callout">
      <div class="callout-label">Call Us Today</div>
      <div class="callout-phone">727.555.0142</div>
    </div>
  </header>
  <nav class="main-nav">
    <a href="#">Home</a><a href="#">Meet the Staff</a><a href="#">Press</a><a href="#">Tour Our Spa</a><a href="#">About</a><a href="#">Blog</a><a href="#">Specials</a><a href="#">Contact</a>
  </nav>
  <div class="hero" role="img" aria-label="Lit candle in a dark bowl of spa stones beside a yellow gerbera and a vase of roses"></div>

  <h1 class="page-title">Blog Post</h1>

  <main class="posts">
    <article class="post">
      <div class="post-media media-massage" role="img" aria-label="Woman relaxing during a back massage"></div>
      <h2 class="post-title">Blog Headline Here</h2>
      <p>Some stress is natural, but often times stress becomes a problem when it leaves you feeling overwhelmed and out of control. Seventy seven percent of Americans report experiencing physical symptoms of stress, according</p>
      <p>In fact, on an average day, 1 million Americans call into work sick for stress-related reasons. Looking for a way to reduce the stress in your life? The answer may lie in a massage with aromatherapy. Both have been scientifically proven to aid people in reducing their feelings of stress and the resulting health issues.</p>
      <p>The National Wellness Research Institute (NWRI) looked at the effects of touch massage on stress responses and found that after five minutes participants' heart rates decreased. Levels of cortisone, a stress-related hormone, were also significantly lowered. An added bonus? Massage has been shown to make people feel better about their bodies, too.</p>
      <div class="share"><span class="s1"></span><span class="s2"></span><span class="s3"></span><span class="s4"></span><span class="s5"></span><span class="s6"></span><span class="count">1</span></div>
      <a class="more" href="#">Learn More</a>
    </article>

    <article class="post">
      <div class="post-media media-fashion" role="img" aria-label="Three runway looks in bright spring colours"></div>
      <h2 class="post-title">Blog Headline Here</h2>
      <p>Have you been paying attention to the latest spring fashion trends? If not, don't worry! We've got you covered from head to toe. This year, the runway trends are actually wearable for work or the weekend. From bold color combos to cool prints, you're sure to feel like a fashionista in any of these new wardrobe ideas.</p>
      <p class="clear">Bright Blazer – There is no better way to enhance your simple black work slacks than with a bright colored blazer. Make a statement in a bold crimson blue or solar power yellow.</p>
      <p>Floral Jeans – Prints are also on trend this spring, especially floral prints. Instead of buying another pair of denim jeans, be adventurous and try on a pair with a print.</p>
      <p>Pastels – Bold colors are hot but pastels are also making a comeback. Lilac and teal are very popular for spring. Before you hit the department store, check your closet for any pastel hues.</p>
      <p class="gap">Colorblocking – This year, bright pink and red can be paired together. So can bright yellow and blue. To colorblock, all you need are two very bold, solid colored separates (shirt and skirt) and pair them together. This trend is hot!</p>
      <div class="share"><span class="s1"></span><span class="s2"></span><span class="s3"></span><span class="s4"></span><span class="s5"></span><span class="s6"></span><span class="count">1</span></div>
      <a class="more" href="#">Learn More</a>
    </article>
  </main>

  <aside class="sidebar">
    <h3>Recent Posts</h3>
    <ul>
      <li>Mauris vel lacus vitae felis vestibulum</li>
      <li>Etiam est nunc venenatis in</li>
      <li>Tristique eu imperdiet ac nisl.</li>
      <li>Cum sociis natoque penatibus</li>
      <li>Et magnis dis parturient montes</li>
    </ul>
    <h3>Archives</h3>
    <ul>
      <li>April 2013</li><li>March 2013</li><li>Feb 2013</li><li>Jan 2013</li>
    </ul>
    <h3>Categories List</h3>
    <ul>
      <li>Phasellus felis</li><li>Dolor scelerisque</li><li>Tempus eget</li><li>Lobortis id libero.</li><li>Donec scelerisque</li><li>Leo ac risus.</li><li>Praesent sit amet est</li><li>In dictum dolor</li><li>Eu dictum porttitor</li><li>Enim felis viverra mi</li>
    </ul>
  </aside>
</div>

<footer class="site-footer">
  <nav class="footer-nav">
    <a href="#">Home</a>|<a href="#">About Us</a>|<a href="#">Spa Services</a>|<a href="#">Spa Packages</a>|<a href="#">Specials</a>|<a href="#">Gift Certificates</a>|<a href="#">Spa Policy</a>|<a href="#">Contact Us</a>
  </nav>
  <p class="copyright">© Copyright 2013 Fernlow Day Spa | 214 Seabreeze Ave. Dunedin, FL 34698</p>
</footer>
<div class="footer-social"><span></span><span></span><span></span></div>
</body>
</html>
```